Small CPA firm
Project: Business cards and stationary
Business cards and stationary - Financial Services
Business cards and stationary
Professional
Darren P. Holcomb
Certified Public Accountant
418 Birchmont Lane, 4-120 Mobile, Alabama 36609
dh@dholcombcpa.example
www.dholcombcpa.example
I'd like a professional but creative looking business card and stationary using my logo. For the business card, I think I would like a design with the logo on the top or the left side, with my name and contact information on the bottom (for logo on top) or right hand side (for logo on left). I'd like to use the same primary colors that the logo uses.
For the back of the card, I think I'd like just the logo without the words in an appropriate format.

```html
<!DOCTYPE html>
<html lang="en">
<head>
<meta charset="utf-8">
<title>Darren P. Holcomb CPA LLC — Business Cards</title>
<link rel="stylesheet" href="https://fonts.googleapis.com/css2?family=Cinzel:wght@400;600&family=Questrial&display=swap">
<style>
  :root {
    --backdrop: #e8e5e1;
    --card-white: #ffffff;
    --ink-slate: #3d4a5c;
    --ink-gray: #4a4a4a;
    --accent-blue: #2f6aa8;
    --accent-deep: #1d4f86;
    --swoosh-gray: #c9cdd2;
    --back-light: #8d8f92;
    --back-dark: #3a3b3d;
    --back-text: #d6d8db;
    --mark-ring: #9aa3ad;
  }
  * { box-sizing: border-box; margin: 0; padding: 0; }
  html, body {
    width: 1200px; height: 576px; overflow: hidden;
    background: var(--backdrop);
  }
  .sheet {
    position: relative; width: 1200px; height: 576px;
  }
  .card {
    position: absolute; top: 74px;
    width: 468px; height: 427px;
    border-radius: 26px; overflow: hidden;
    box-shadow: 0 4px 14px rgba(0,0,0,0.18);
  }
  .card-front { left: 120px; background: var(--card-white); }
  .card-back {
    left: 629px;
    background: radial-gradient(ellipse at 50% 45%, var(--back-light) 0%, #616366 45%, var(--back-dark) 100%);
  }

  .brand {
    position: absolute; left: 28px; top: 22px;
    display: flex; align-items: center; gap: 14px;
  }
  .brand-dot {
    width: 76px; height: 76px; border-radius: 50%;
    border: 3px solid var(--accent-blue);
    flex: none;
  }
  .brand-text { color: var(--ink-slate); font-family: "Cinzel", serif; }
  .brand-name { font-size: 21px; font-weight: 400; line-height: 1.15; }
  .brand-tagline { font-size: 13.5px; margin-top: 4px; letter-spacing: 0.2px; }

  .contact {
    position: absolute; left: 0; right: 0; top: 160px;
    text-align: center;
    font-family: "Questrial", sans-serif; color: var(--ink-gray);
  }
  .contact-name { font-size: 16px; color: var(--accent-deep); letter-spacing: 0.5px; }
  .contact-title { font-size: 13px; margin-top: 6px; }
  .contact-address { font-size: 13px; margin-top: 26px; }
  .contact-lines { margin-top: 14px; font-size: 12.5px; line-height: 1.75; }
  .contact-lines .label { color: var(--accent-blue); }
  .contact-lines .gap { display: inline-block; width: 16px; }

  .swoosh { position: absolute; left: 0; bottom: 0; width: 468px; height: 96px; display: block; }

  .back-mark {
    position: absolute; left: 50%; top: 150px;
    width: 86px; height: 86px; margin-left: -43px;
    border-radius: 50%;
    border: 4px solid var(--mark-ring);
    background: radial-gradient(circle at 40% 35%, #7d8186, #4a4c50);
  }
  .back-url {
    position: absolute; left: 0; right: 0; top: 335px;
    text-align: center;
    font-family: "Questrial", sans-serif; font-size: 12.5px;
    letter-spacing: 2.5px; color: var(--back-text);
  }
</style>
</head>
<body>
<main class="sheet">
  <section class="card card-front" aria-label="Business card front">
    <header class="brand">
      <span class="brand-dot"></span>
      <div class="brand-text">
        <div class="brand-name">Darren P. Holcomb CPA LLC</div>
        <div class="brand-tagline">Certified Public Accountant and Advisor</div>
      </div>
    </header>

    <div class="contact">
      <div class="contact-name">DARREN P. HOLCOMB</div>
      <div class="contact-title">Certified Public Accountant</div>
      <div class="contact-address">418 Birchmont Lane, 4-120 Mobile, Alabama 36609</div>
      <div class="contact-lines">
        <div><span class="label">Ph.:</span> (251) 555-0142<span class="gap"></span><span class="label">C.:</span> (251) 555-0187</div>
        <div><span class="label">F.:</span> (251) 555-0163<span class="gap"></span><span class="label">E.:</span> dh@dholcombcpa.example</div>
      </div>
    </div>

    <svg class="swoosh" viewBox="0 0 468 96" preserveAspectRatio="none" aria-hidden="true">
      <defs>
        <linearGradient id="swooshBlue" x1="0" y1="0" x2="1" y2="0">
          <stop offset="0" stop-color="#1d4f86"/>
          <stop offset="0.6" stop-color="#3a7cc0"/>
          <stop offset="1" stop-color="#6fa6d8"/>
        </linearGradient>
        <linearGradient id="swooshGray" x1="0" y1="0" x2="0" y2="1">
          <stop offset="0" stop-color="#e2e5e8"/>
          <stop offset="1" stop-color="#b8bdc3"/>
        </linearGradient>
      </defs>
      <path d="M0 40 C 120 78, 300 70, 468 20 L468 96 L0 96 Z" fill="url(#swooshBlue)"/>
      <path d="M0 58 C 140 92, 320 84, 468 38 L468 96 L0 96 Z" fill="url(#swooshGray)"/>
      <path d="M0 58 C 140 92, 320 84, 468 38" fill="none" stroke="#ffffff" stroke-width="2"/>
    </svg>
  </section>

  <section class="card card-back" aria-label="Business card back">
    <span class="back-mark"></span>
    <div class="back-url">www.dholcombcpa.example</div>
  </section>
</main>
</body>
</html>
```